Improve Wine Bottle Label, Glass Printed Naked Lady, Elegant, Classy, Professional

We are transitioning our labelling method over to glass screen-printing.We have an existing label (attached image1 -ai also attached) that we think is cool, but moving forward we would like a more professional looking design that is classy, artsy, but still high impact (one very rough idea is attached). The bottle is remaining the same size. The cap is the same pink colour. Title of wine is The Quiet Harbour' Front Text needs to include:2018 MontepulcianoEden Valley - Barossa The graphic must contain a tasteful (arty) and attractive naked woman. Design colours that are preferred are:Hot Pink - as seen in imageDark Blue - as seen in imageMatte White** Note that colours are single, shading etc is not easily possible due to the screen printing method. - view process on our instagram page. https://www.instagram.com/tvelwinehouse/- please also look at this page to see our other recent labels, so ascertain our style/audience.You do not need to have all the colours, if your submission looks great with 1 or 2. feel free to keep it this way. Dimensions.The glass printer can print within 10mm of the base of the bottle, and 10mm of the shoulder of the bottle. Height 150mmIt can print the full circumference of the bottle up to approx 30mm gap. (Max 208mm) - see our gold label on the instagram page. - however, imagine this bottle in a store - we need customers to be able to see the image and title on one side. So if you decide to wrap around the bottle, it needs to achieve the requirements whilst only seeing the Title side of the bottle. We have found this to be about 90mm wide maximum.

Target Market(s)

Wine Consumers

Industry/Entity Type

Winery

Font styles to use
Serif
Sans Serif

Colors
e34297
3176b5
ffffff

Requirements
Must have
• Colours, Title, Text - as stated
• Naked arty woman
• Single colours - NO SHADING
Nice to have
• Our Logo integrated smoothly - only do this if you can do it well.

```html
<!DOCTYPE html>
<html lang="en">
<head>
<meta charset="utf-8">
<title>The Quiet Harbour' – Glass Print Label</title>
<link rel="stylesheet" href="https://fonts.googleapis.com/css2?family=Dosis:wght@300;400;500;700&display=swap">
<style>
  :root {
    --bg: #232323;
    --glass: #161616;
    --pink: #e34297;
    --blue: #3176b5;
    --white: #f2f2f2;
    --muted: #bdbdbd;
  }
  * { margin: 0; padding: 0; box-sizing: border-box; }
  html, body { width: 1200px; height: 917px; overflow: hidden; }
  body {
    background: var(--bg);
    font-family: "Dosis", Arial, sans-serif;
    color: var(--white);
    position: relative;
  }
  .label {
    position: absolute;
    top: 150px;
    width: 320px;
    height: 620px;
    background: var(--glass);
    border-radius: 6px;
    overflow: hidden;
  }
  .label--front { left: 230px; }
  .label--back { left: 650px; }

  /* Front */
  .front-title {
    position: absolute;
    left: 22px;
    bottom: 110px;
    writing-mode: vertical-rl;
    transform: rotate(180deg);
    font-size: 50px;
    font-weight: 300;
    letter-spacing: 1px;
    white-space: nowrap;
    line-height: 1;
  }
  .front-figure {
    position: absolute;
    left: 92px;
    top: 120px;
    width: 150px;
    height: 400px;
  }
  .front-abv {
    position: absolute;
    left: 88px;
    top: 528px;
    writing-mode: vertical-rl;
    font-size: 12px;
    font-weight: 500;
    line-height: 1.2;
  }
  .front-abv small { font-size: 7px; letter-spacing: .5px; }
  .front-vintage {
    position: absolute;
    left: 250px;
    top: 330px;
    writing-mode: vertical-rl;
    font-size: 18px;
    font-weight: 400;
    line-height: 1.05;
    white-space: nowrap;
  }

  /* Back */
  .back {
    position: absolute;
    inset: 0;
    text-align: center;
    padding: 140px 24px 0;
  }
  .back-title {
    font-size: 30px;
    font-weight: 300;
    letter-spacing: .5px;
    line-height: 1;
    white-space: nowrap;
    margin-bottom: 14px;
  }
  .back-copy {
    font-size: 8.5px;
    line-height: 1.45;
    color: var(--muted);
    margin: 0 8px 10px;
  }
  .brand {
    display: inline-flex;
    align-items: center;
    gap: 6px;
    margin: 8px 0 12px;
  }
  .brand-dot {
    width: 14px; height: 14px;
    border: 1.5px solid var(--white);
    border-radius: 50%;
  }
  .brand-name { font-size: 22px; font-weight: 400; }
  .origin { font-size: 11px; letter-spacing: .5px; }
  .web { font-size: 9px; color: var(--muted); margin: 3px 0 10px; }
  .social {
    display: flex;
    justify-content: center;
    gap: 5px;
    text-align: left;
    font-size: 8.5px;
    line-height: 1.25;
    color: var(--muted);
  }
  .social-square { width: 12px; height: 12px; background: var(--white); margin-top: 2px; }
  .facts {
    display: flex;
    justify-content: center;
    align-items: flex-end;
    gap: 30px;
    margin-top: 22px;
  }
  .facts-volume { text-align: left; line-height: 1.1; }
  .facts-volume .abv { font-size: 11px; font-weight: 500; }
  .facts-volume .ml { font-size: 19px; font-weight: 700; }
  .std-drinks { display: flex; align-items: flex-end; gap: 3px; }
  .std-drinks-label {
    writing-mode: vertical-rl;
    transform: rotate(180deg);
    font-size: 7px;
    color: var(--muted);
  }
</style>
</head>
<body>

<section class="label label--front">
  <h1 class="front-title">THE QUIET HARBOUR'</h1>

  <svg class="front-figure" viewBox="0 0 150 400" role="img" aria-label="Single-colour screen-printed line art of a standing nude woman draped in fabric, hot pink">
    <rect width="150" height="400" rx="4" fill="#e34297"/>
  </svg>

  <p class="front-abv">14% ALC/VOL<br><small>ENJOY RESPONSIBLY</small></p>
  <p class="front-vintage">2018 MONTEPULCIANO<br>EDEN VALLEY - BAROSSA</p>
</section>

<section class="label label--back">
  <div class="back">
    <h2 class="back-title">THE QUIET HARBOUR'</h2>
    <p class="back-copy">Lorem ipsum dolor sit amet, consectetur adipiscing elit, sed do eiusmod tempor incididunt ut labore et dolore magna aliqua. Ut enim ad minim veniam, quis nostrud exercitation ullamco laboris nisi ut aliquip ex ea commodo consequat.</p>
    <p class="back-copy">et dolore magna aliqua.<br>Ut enim ad minim veniam, quis nostrud exercitation ullamco laboris nisi ut aliquip ex ea commodo consequat.</p>

    <div class="brand">
      <span class="brand-dot"></span>
      <span class="brand-name">Tvel</span>
    </div>

    <p class="origin">WINE OF AUSTRALIA</p>
    <p class="web">tvelwinehouse.com.au</p>

    <div class="social">
      <span class="social-square"></span>
      <p>Find us on Socials<br>Tvel Wine House Sales</p>
    </div>

    <div class="facts">
      <div class="facts-volume">
        <p class="abv">15.4% ALC/VOL</p>
        <p class="ml">750mL</p>
      </div>
      <div class="std-drinks">
        <span class="std-drinks-label">Standard Drinks</span>
        <svg width="24" height="40" viewBox="0 0 24 40" aria-label="9.1 standard drinks">
          <path d="M3 2 H21 L19 17 Q12 22 5 17 Z" fill="none" stroke="#f2f2f2" stroke-width="1.5"/>
          <line x1="12" y1="20" x2="12" y2="36" stroke="#f2f2f2" stroke-width="1.5"/>
          <line x1="5" y1="37" x2="19" y2="37" stroke="#f2f2f2" stroke-width="1.5"/>
          <text x="12" y="13" text-anchor="middle" font-family="Dosis, sans-serif" font-size="8" fill="#f2f2f2">9.1</text>
        </svg>
      </div>
    </div>
  </div>
</section>

</body>
</html>
```